"Torvek Industries" needs a creative design

We need a Business card design for a new company based in Australia : Melbourne called "Torvek Industries"

The company will primary be importing Furniture . ie Replica Furniture, Home furniture, Office Furniture, Outdoor Furniture and Entertainment Units

We would like to see the design that use the color Champion Red / Platinum Silver on the Logo .

The final design should communicate " Great quality furniture, Best prices and good customer service"

Also in the Business card please add the following info
- ABN : 52384017265
- Email Address : Torvek.Industires@Mailpoint.com
- WebSite : www.TorvekIndustries.com.au
- FB (Socialpage icon) : [TorvekIndustries] Like us on Socialpage [like hand]
- PH : 0472 916 358

Please refer to attachment for the logo

Sans Serif

eb1f27
1b1b1b
5c5c5c
f5f5f5
f04a50

```html
<!DOCTYPE html>
<html lang="en">
<head>
<meta charset="utf-8">
<title>Torvek Industries – Business Card</title>
<link rel="stylesheet" href="https://fonts.googleapis.com/css2?family=Cinzel:wght@700&family=Open+Sans:ital,wght@0,700;1,700&display=swap">
<style>
  :root {
    --champion-red: #eb1f27;
    --soft-red: #f04a50;
    --ink: #1b1b1b;
    --platinum: #5c5c5c;
    --mist: #f5f5f5;
    --band-grey: #e2e2e2;
    --paper: #ffffff;
    --table: #d9d9d9;
    --social-blue: #3b5998;
  }
  * { margin: 0; padding: 0; box-sizing: border-box; }
  html, body {
    width: 1200px; height: 1200px; overflow: hidden;
    background: var(--table);
  }
  .sheet {
    position: relative; width: 1200px; height: 1200px;
  }
  .card {
    position: absolute; left: 160px; width: 880px; height: 490px;
    background: var(--paper);
    box-shadow: 0 6px 18px rgba(0,0,0,0.18);
    overflow: hidden;
  }
  .card--front { top: 80px; }
  .card--back { top: 630px; }

  .brand {
    position: absolute; display: flex; align-items: center;
  }
  .brand__square {
    background: var(--champion-red);
    flex: none;
  }
  .brand__name {
    font-family: "Cinzel", serif; font-weight: 700;
    color: var(--champion-red); line-height: 1.05;
    text-transform: uppercase;
  }
  .card--front .brand { left: 50%; top: 50%; transform: translate(-50%, -50%); gap: 30px; }
  .card--front .brand__square { width: 96px; height: 96px; }
  .card--front .brand__name { font-size: 58px; }

  .card--back .brand { right: 50px; top: 48px; gap: 18px; }
  .card--back .brand__square { width: 52px; height: 52px; }
  .card--back .brand__name { font-size: 32px; }

  .waves { position: absolute; inset: 0; width: 880px; height: 490px; }

  .contact {
    position: absolute; left: 40px; top: 232px;
    list-style: none;
    font-family: "Open Sans", sans-serif; font-style: italic; font-weight: 700;
    font-size: 21px; color: var(--paper); line-height: 40px;
  }
  .social {
    position: absolute; left: 230px; top: 408px;
    width: 500px; height: 52px; border-radius: 10px;
    background: var(--paper);
    display: flex; align-items: center; justify-content: center; gap: 10px;
    font-family: "Open Sans", sans-serif; font-weight: 700; font-size: 21px;
  }
  .social__network { color: var(--social-blue); font-size: 24px; }
  .social__handle { color: var(--champion-red); }
  .social__mark { width: 20px; height: 20px; background: var(--social-blue); border-radius: 3px; }
</style>
</head>
<body>
<main class="sheet">
  <section class="card card--front">
    <div class="brand">
      <span class="brand__square"></span>
      <span class="brand__name">Torvek<br>Industries</span>
    </div>
  </section>

  <section class="card card--back">
    <svg class="waves" viewBox="0 0 880 490" aria-hidden="true">
      <path d="M80,0 C330,20 600,250 880,330 L880,490 L0,490 L0,0 Z" fill="var(--band-grey)"/>
      <path d="M45,0 C300,25 560,300 880,410 L880,490 L0,490 L0,0 Z" fill="var(--soft-red)"/>
      <path d="M0,0 L20,0 C270,40 520,330 820,490 L0,490 Z" fill="var(--champion-red)"/>
    </svg>

    <div class="brand">
      <span class="brand__square"></span>
      <span class="brand__name">Torvek<br>Industries</span>
    </div>

    <ul class="contact">
      <li>Phone : 0472 916 358</li>
      <li>ABN : 52384017265</li>
      <li>Email : Torvek.Industires@Mailpoint.com</li>
      <li>Web : www.TorvekIndustries.com.au</li>
    </ul>

    <div class="social">
      <span class="social__network">Socialpage</span>
      <span class="social__handle">: TORVEKINDUSTRIES</span>
      <span class="social__mark"></span>
    </div>
  </section>
</main>
</body>
</html>
```